Corvane Networks web design

Corvane is an Internet Service Provider bringing high-speed service to homes and businesses. Our principal market target is rural areas of West Michigan, but we intend to expand rapidly. We need a website to market our services, facilitate online ordering, customer support and communicate with our customers.

I will upload a draft outline of the content we hope to include in the website.

We compete directly with Halberd Communications, Lumetra, Dravix and Kelwick communications to bring Internet service to homes and businesses in our coverage area.

Our primary values include:

1. Unlike our competitors, we do not require long term contractors or service bundles; There are no termination fees, for example. All services are sold on a recurring 1-month agreement term.
2. Unlike other wireless (mobile) providers, we do not limit downloads or uploads with bit/byte buckets
3. We provide service to areas ignored by the larger carriers - Rural areas in Michigan that lack options for broadband are prime targets for Corvane to cover.
4. Unlike other wireless ISP's, we utilize licensed FCC spectrum. We do not use unlicensed/free frequencies, providing us an advantage for reliability and stability.
Updates

So many wonderful designs, thank you very much for all your hard work. We are evaluating all our favorite designs and plan to make a selection in the next 2 days. I will be in touch with you to request revisions if necessary or further refinements.  Thank you again for your efforts on this project.

Target Market(s)

Our target market is home Internet users. however, that does not mean that our users are "high tech" oriented - they are just normal mom's and pop's who buy Internet for home use. The site should be easy to navigate and communicate our message of speed, value, reliability and facilitate simple product ordering.

Industry/Entity Type

Internet

Requirements
Must have
• Our phone number should be prominently displayed 1-844-7NU-LINK
• Our logo is uploaded in the attachments.
• Design for desktop and mobile devices.
Nice to have
• The most modern of web design trends. Such as a design that facilitates parallax scrolling effects rather than lots of individual pages.
• Stock artwork communicating our values of speed and reliability.

```html
<!DOCTYPE html>
<html lang="en">
<head>
<meta charset="utf-8">
<title>Corvane Networks – West Michigan's Best Internet Service</title>
<link href="https://fonts.googleapis.com/css2?family=Open+Sans:wght@300;400;600;700;800&display=swap" rel="stylesheet">
<style>
  :root {
    --topbar-bg: #eeeeee;
    --topbar-text: #6f6f6f;
    --divider: #d6d6d6;
    --white: #ffffff;
    --orange: #f0883a;
    --nav-text: #4a4a4a;
    --navy: rgba(40, 55, 72, 0.92);
    --blue: #4aa8cf;
    --hero-dark: #2b2a28;
  }
  * { box-sizing: border-box; margin: 0; padding: 0; }
  html, body { width: 1200px; height: 734px; overflow: hidden; }
  body { font-family: "Open Sans", Arial, sans-serif; background: var(--white); position: relative; }

  .topbar {
    position: absolute; left: 0; top: 0; width: 1200px; height: 37px;
    background: var(--topbar-bg); display: flex; align-items: center; justify-content: flex-end;
    padding-right: 286px;
  }
  .topbar-link {
    display: flex; align-items: center; gap: 6px; height: 37px; padding: 0 14px;
    font-size: 10px; font-weight: 700; color: var(--topbar-text); letter-spacing: .3px;
    border-left: 1px solid var(--divider);
  }
  .topbar-link svg { width: 11px; height: 11px; }
  .search-field {
    width: 92px; height: 37px; background: var(--white); border-left: 1px solid var(--divider);
    font-size: 10px; color: #a8a8a8; display: flex; align-items: center; padding-left: 9px;
  }
  .search-button {
    width: 38px; height: 37px; background: var(--orange); display: flex; align-items: center; justify-content: center;
  }

  .main-nav {
    position: absolute; left: 0; top: 37px; width: 1200px; height: 62px; background: var(--white);
  }
  .brand {
    position: absolute; left: 286px; top: 17px; display: flex; align-items: center; gap: 8px;
    font-size: 19px; font-weight: 700; color: var(--orange); letter-spacing: .5px;
  }
  .brand-dot { width: 12px; height: 12px; border-radius: 50%; background: var(--orange); }
  .nav-link { position: absolute; top: 21px; font-size: 13px; color: var(--nav-text); }
  .nav-link.active { color: var(--orange); }

  .hero {
    position: absolute; left: 0; top: 99px; width: 1200px; height: 635px;
    background:
      radial-gradient(ellipse 300px 220px at 690px 160px, rgba(96,128,80,.75), transparent 70%),
      radial-gradient(ellipse 260px 200px at 960px 120px, rgba(120,150,170,.55), transparent 70%),
      radial-gradient(ellipse 220px 260px at 140px 260px, rgba(150,130,110,.5), transparent 70%),
      linear-gradient(180deg, #3b3a36 0%, #2f2e2b 55%, #4a4743 100%);
  }
  .hero-title {
    position: absolute; left: 0; top: 150px; width: 1200px; padding-left: 0;
    text-align: center; font-size: 33px; font-weight: 700; color: var(--white);
    text-shadow: 0 2px 6px rgba(0,0,0,.45);
  }
  .hero-title span { position: relative; left: -3px; }

  .coverage-box {
    position: absolute; left: 287px; top: 339px; width: 261px; height: 248px; background: var(--navy);
    padding: 22px 14px 0;
  }
  .coverage-box h2 { font-size: 19px; font-weight: 700; color: var(--white); }
  .coverage-box p { margin-top: 20px; font-size: 14.5px; line-height: 1.3; color: var(--white); }
  .address-field {
    margin-top: 26px; height: 42px; background: var(--white); font-size: 13px; color: #a8a8a8;
    display: flex; align-items: center; padding-left: 12px;
  }
  .submit-button {
    margin-top: 17px; height: 44px; background: var(--blue); color: var(--white);
    font-size: 14px; font-weight: 700; display: flex; align-items: center; justify-content: center;
  }
  .or-divider {
    position: absolute; left: 566px; top: 509px; font-size: 20px; font-weight: 700; color: var(--white);
  }

  .benefits { position: absolute; left: 648px; top: 264px; color: var(--white); }
  .benefits h3 { font-size: 23px; font-weight: 700; }
  .benefit-list { list-style: none; margin-top: 14px; }
  .benefit-list li { display: flex; align-items: center; gap: 12px; font-size: 25px; font-weight: 400; height: 36px; }
  .benefit-list svg { width: 20px; height: 20px; }

  .order-box {
    position: absolute; left: 650px; top: 464px; width: 260px; height: 122px; background: var(--orange);
    padding: 18px 24px 0; color: var(--white);
  }
  .order-box .order-label { font-size: 23px; font-weight: 300; }
  .order-box .order-phone { margin-top: 8px; font-size: 30px; font-weight: 700; letter-spacing: .3px; }
</style>
</head>
<body>
  <header>
    <div class="topbar">
      <div class="topbar-link">
        <svg viewBox="0 0 12 12" fill="none" stroke="#7a7a7a" stroke-width="1.2"><rect x="1.5" y="1.5" width="9" height="9"/><line x1="3.5" y1="4.5" x2="8.5" y2="4.5"/><line x1="3.5" y1="7" x2="8.5" y2="7"/></svg>BLOG
      </div>
      <div class="topbar-link">
        <svg viewBox="0 0 12 12" fill="none" stroke="#7a7a7a" stroke-width="1.2"><path d="M2 2h8v6H5l-3 2z"/></svg>CUSTOMERS
      </div>
      <div class="topbar-link">
        <svg viewBox="0 0 12 12" fill="none" stroke="#7a7a7a" stroke-width="1.2"><circle cx="6" cy="4" r="2.3"/><path d="M1.8 11c.6-2.6 2.2-3.6 4.2-3.6s3.6 1 4.2 3.6"/></svg>ACCOUNT
      </div>
      <div class="search-field">Search...</div>
      <div class="search-button">
        <svg width="12" height="12" viewBox="0 0 12 12" fill="none" stroke="#fff" stroke-width="1.6"><circle cx="5" cy="5" r="3.3"/><line x1="7.5" y1="7.5" x2="10.5" y2="10.5"/></svg>
      </div>
    </div>
    <nav class="main-nav">
      <div class="brand"><span class="brand-dot"></span>Corvane Networks</div>
      <span class="nav-link active" style="left:515px">Home</span>
      <span class="nav-link" style="left:597px">Service Plans</span>
      <span class="nav-link" style="left:719px">Coverage Map</span>
      <span class="nav-link" style="left:843px">About us</span>
    </nav>
  </header>

  <main class="hero" role="img" aria-label="Blurred photo of a family watching a streaming show on a large living-room TV">
    <h1 class="hero-title"><span>West Michigan’s Best Internet Service</span></h1>

    <section class="coverage-box">
      <h2>AM I COVERED?</h2>
      <p>Enter &nbsp;Your address to check for service availability</p>
      <div class="address-field">Enter your address...</div>
      <div class="submit-button">SUBMIT</div>
    </section>

    <div class="or-divider">- OR -</div>

    <section class="benefits">
      <h3>Why we’re better?</h3>
      <ul class="benefit-list">
        <li><svg viewBox="0 0 20 20" fill="none" stroke="#fff" stroke-width="1.6"><circle cx="10" cy="10" r="7.5"/><line x1="10" y1="10" x2="13" y2="6.5"/></svg>Faster Speed</li>
        <li><svg viewBox="0 0 20 20" fill="none" stroke="#fff" stroke-width="1.6"><circle cx="10" cy="10" r="7.5"/><line x1="4.8" y1="4.8" x2="15.2" y2="15.2"/></svg>No Limits</li>
        <li><svg viewBox="0 0 20 20" fill="#fff"><ellipse cx="10" cy="5" rx="7" ry="2.6"/><ellipse cx="10" cy="10" rx="7" ry="2.6"/><ellipse cx="10" cy="15" rx="7" ry="2.6"/></svg>More Value</li>
      </ul>
    </section>

    <section class="order-box">
      <div class="order-label">ORDER NOW</div>
      <div class="order-phone">844-7NU-LINK</div>
    </section>
  </main>
</body>
</html>
```